Web Design for Financial Consulting Company

We need a website design for a financial consulting company "Kelvane Consulting". We build financial models, scenario analysis, handle the budgeting process and provide temporary staffing. I have over 10 years of experience. My Excel expertise and analytical savvy has saved clients over $17 million in profit.

Target Market(s)

Small to medium businesses

Industry/Entity Type

Financial Consulting

Number of Pages Required

4 page

Requirements
Must have
• Professional looking
Nice to have
• A little futuristic looking

```html
<!DOCTYPE html>
<html lang="en">
<head>
<meta charset="utf-8">
<title>Kelvane Consulting – Home Page</title>
<link href="https://fonts.googleapis.com/css2?family=Cinzel:wght@500&family=Michroma&family=Open+Sans:wght@400;600;700&family=Great+Vibes&display=swap" rel="stylesheet">
<style>
:root{
  --blue:#1a9be6;
  --blue-deep:#0d7fcf;
  --navy:#111c27;
  --navy-2:#172532;
  --ink:#1d2630;
  --muted:#5d6770;
  --line:#c9d2da;
  --white:#ffffff;
  --bg-a:#0f1c26;
  --bg-b:#1787d2;
}
*{margin:0;padding:0;box-sizing:border-box}
html,body{width:1200px;height:3989px;overflow:hidden}
body{background:linear-gradient(135deg,var(--bg-a) 0%,#13324a 45%,var(--bg-b) 100%);font-family:"Open Sans",sans-serif;color:var(--ink);position:relative}
.board-title{position:absolute;font-family:"Cinzel",serif;color:var(--white);font-weight:500;white-space:nowrap}
.board-title--page{top:705px;left:0;width:1200px;text-align:center;font-size:62px;letter-spacing:2px}
.board-title--mobile{top:822px;left:90px;font-size:31px}
.board-title--web{top:810px;left:580px;font-size:62px}
.board-thanks{position:absolute;top:3850px;left:0;width:1200px;text-align:center;font-family:"Great Vibes",cursive;font-size:86px;color:var(--white)}

.head{font-family:"Michroma",sans-serif;text-transform:uppercase;line-height:1.3}
.accent{color:var(--blue)}
.kicker{font-size:5px;letter-spacing:5px;color:var(--blue);text-transform:uppercase;text-align:center}
.body-text{font-size:5.5px;line-height:1.75}
.btn{display:inline-block;font-size:5.5px;font-weight:600;text-transform:uppercase;padding:4px 10px;border:1px solid var(--blue);color:var(--blue);background:transparent}
.btn--solid{background:var(--blue);color:var(--white)}
.btn--light{border-color:var(--white);color:var(--white)}
.photo{display:block}
.brand{display:flex;align-items:center;gap:5px;font-family:"Open Sans",sans-serif;font-weight:700;font-size:10px;letter-spacing:1px;text-transform:uppercase;white-space:nowrap}
.brand-mark{width:12px;height:12px;border:2px solid var(--blue)}
.icon{width:9px;height:9px;flex:none}

/* ---------- WEB ---------- */
.site{position:absolute;width:680px;overflow:hidden}
.site--dark{top:889px;left:464px}
.site--light{top:2334px;left:462px}
.sec{position:relative;width:680px}
.topbar{height:15px;background:var(--navy)}
.site--light .topbar{background:var(--white)}
.topbar-blue{position:absolute;left:0;top:0;height:15px;width:310px;background:var(--blue);clip-path:polygon(0 0,100% 0,96% 100%,0 100%)}
.socials{position:absolute;display:flex;gap:4px}
.socials span{width:8px;height:8px;background:var(--white);display:block}
.topbar .socials{left:92px;top:3.5px}
.topbar-info{position:absolute;right:95px;top:3px;display:flex;gap:12px;font-size:5.5px;color:var(--white)}
.site--light .topbar-info{color:var(--ink)}
.nav{height:36px;background:var(--navy);color:var(--white)}
.site--light .nav{background:var(--white);color:var(--ink)}
.nav-links{position:absolute;top:14px;display:flex;gap:20px;font-size:6px}
.nav-links--left{left:92px}
.nav-links--right{left:430px;align-items:center;top:11px}
.nav .brand{position:absolute;left:287px;top:11px;font-size:10px}
.hero{height:319px}
.site--light .hero{height:324px}
.hero-photo{position:absolute;inset:0;background:linear-gradient(100deg,#f2f4f6 0%,#e5e9ed 40%,#c3ccd4 70%,#7f8a93 100%)}
.hero-copy{position:absolute;left:90px;top:68px;width:300px}
.hero-copy .head{font-size:22px;color:var(--ink)}
.hero-copy .body-text{width:250px;margin:6px 0 12px;color:var(--muted)}
.hero-dots{position:absolute;left:26px;top:110px;display:flex;flex-direction:column;gap:9px}
.hero-dots span{width:3px;height:3px;border-radius:50%;background:var(--white)}
.hero-dots span.on{background:var(--blue)}
.services{height:336px;background:var(--navy);color:var(--white);text-align:center}
.site--light .services{height:341px;background:var(--white);color:var(--ink)}
.sec-title{font-size:20px;padding-top:30px}
.cards{position:absolute;left:93px;top:80px;display:flex;gap:10px}
.card{width:116px;text-align:center}
.card .photo{width:116px;height:105px}
.card h3{font-size:6.5px;font-weight:600;text-transform:uppercase;margin:10px 0 4px}
.card .body-text{margin-bottom:9px}
.services .more{position:absolute;left:0;right:0;top:290px}
.about{height:263px;background:linear-gradient(120deg,#1b8fdc 0%,#1ea3ec 60%,#168bd6 100%);color:var(--white)}
.site--light .about{height:268px}
.about .photo{position:absolute;left:93px;top:34px;width:195px;height:182px}
.about-badge{position:absolute;left:248px;top:168px;width:54px;height:54px;background:var(--blue);border:4px solid var(--white)}
.about-copy{position:absolute;left:328px;top:36px;width:260px}
.about-copy .head{font-size:20px}
.about-copy .kicker{color:var(--white);text-align:left;margin:4px 0 8px}
.about-copy .body-text{margin-bottom:7px}
.contact{height:240px;background:var(--navy);color:var(--white)}
.site--light .contact{height:252px;background:var(--white);color:var(--ink)}
.contact .sec-title{text-align:center;padding-top:30px}
.contact .kicker{margin-top:3px}
.contact-info{position:absolute;left:93px;top:95px;display:flex;flex-direction:column;gap:14px;font-size:6px}
.contact-info div{display:flex;gap:8px;align-items:flex-start;line-height:1.6}
.form{position:absolute;left:289px;top:80px;width:300px;display:grid;grid-template-columns:1fr 1fr;gap:8px 6px}
.field{height:20px;border:1px solid var(--line);background:var(--white);font-size:5px;color:#8a949c;padding:5px 4px}
.site--dark .field{background:transparent;border-color:#54606b;color:#aab3bb}
.field--msg{grid-column:1/3;height:46px}
.form .submit{grid-column:1/3;justify-self:center;margin-top:4px}
.footer{height:203px;background:var(--navy-2);color:var(--white);text-align:center}
.site--light .footer{height:209px;background:var(--navy)}
.footer .brand{position:absolute;left:274px;top:38px;font-size:12px}
.footer-info{position:absolute;top:80px;left:100px;width:480px;display:flex;justify-content:space-between;font-size:5.5px;text-align:left}
.footer-info div{display:flex;gap:6px;align-items:center}
.dot-icon{width:16px;height:16px;border-radius:50%;background:var(--blue);flex:none;display:flex;align-items:center;justify-content:center}
.footer-rule{position:absolute;left:93px;width:494px;height:1px;background:#3c4955}
.footer-links{position:absolute;top:124px;left:0;right:0;display:flex;justify-content:center;gap:18px;font-size:5.5px;font-weight:700;text-transform:uppercase}
.copy{position:absolute;top:160px;left:0;right:0;font-size:5.5px}
.footer .socials{top:178px;left:307px;gap:8px}

/* ---------- MOBILE ---------- */
.mobile{position:absolute;top:890px;left:147px;width:167px;overflow:hidden}
.m-sec{position:relative;width:167px}
.m-header{height:26px;background:var(--white)}
.m-header .brand{position:absolute;left:8px;top:7px;font-size:9px}
.m-burger{position:absolute;right:8px;top:9px;width:9px;height:8px;border-top:2px solid var(--ink);border-bottom:2px solid var(--ink)}
.m-burger::after{content:"";position:absolute;left:0;right:0;top:1px;height:2px;background:var(--ink)}
.m-hero{height:180px}
.m-hero .hero-photo{background:linear-gradient(180deg,#f4f6f8 0%,#e4e8ec 45%,#aeb8c1 100%)}
.m-hero-copy{position:absolute;left:16px;top:12px}
.m-hero-copy .head{font-size:10px;color:var(--ink)}
.m-hero-copy .btn{font-size:4px;padding:2px 6px;margin-top:4px}
.m-services{height:1022px;background:var(--white);text-align:center}
.m-services .sec-title{font-size:12px;padding-top:22px}
.m-card{position:absolute;left:18px;width:131px;text-align:center}
.m-card .photo{width:131px;height:124px}
.m-card h3{font-size:7.5px;font-weight:600;text-transform:uppercase;margin:10px 0 4px}
.m-card .body-text{font-size:5.5px;margin-bottom:8px}
.m-services .more{position:absolute;left:0;right:0;top:984px}
.m-about{height:483px;background:linear-gradient(160deg,#1ea3ec 0%,#1890dd 100%);color:var(--white);text-align:center}
.m-about .head{font-size:12px;padding-top:38px}
.m-about .kicker{color:var(--white);margin:5px 0 10px}
.m-about .body-text{padding:0 12px;margin-bottom:10px}
.m-about .photo{position:absolute;left:8px;top:313px;width:147px;height:132px}
.m-about .about-badge{left:118px;top:408px;width:36px;height:36px;border-width:3px}
.m-contact{height:418px;background:var(--white)}
.m-contact .head{font-size:13px;padding:28px 0 0 20px}
.m-contact .kicker{text-align:left;padding-left:28px;margin-top:3px}
.m-info{position:absolute;left:12px;top:70px;display:flex;flex-direction:column;gap:16px;font-size:6px}
.m-info div{display:flex;gap:9px;line-height:1.6}
.m-form{position:absolute;left:12px;top:165px;width:143px;display:flex;flex-direction:column;gap:13px}
.m-form .field{height:21px}
.m-form .field--msg{height:53px}
.m-form .submit{align-self:center}
.m-footer{height:356px;background:var(--navy);color:var(--white);text-align:center}
.m-footer .brand{position:absolute;left:26px;top:36px;font-size:9px}
.m-finfo{position:absolute;left:14px;top:70px;display:flex;flex-direction:column;gap:12px;font-size:5.5px;text-align:left}
.m-finfo div{display:flex;gap:7px;align-items:center}
.m-footer .footer-rule{left:8px;width:151px}
.m-flinks{position:absolute;top:174px;left:0;right:0;display:flex;flex-direction:column;gap:11px;font-size:6px;font-weight:700}
.m-footer .copy{top:302px;font-size:5px;line-height:1.7}
.m-footer .socials{top:330px;left:46px;gap:11px}
</style>
</head>
<body>

<h1 class="board-title board-title--page">HOME PAGE</h1>
<h2 class="board-title board-title--mobile">MOBILE VERSION</h2>
<h2 class="board-title board-title--web">WEB VERSION</h2>

<!-- ================= MOBILE ================= -->
<div class="mobile">
  <header class="m-sec m-header">
    <div class="brand"><span class="brand-mark"></span><span>Kelvane Consulting</span></div>
    <span class="m-burger"></span>
  </header>
  <section class="m-sec m-hero">
    <div class="hero-photo" role="img" aria-label="Photo of a smiling businesswoman at a laptop with a colleague in an office"></div>
    <div class="m-hero-copy">
      <p class="head">Helping <span class="accent">your</span><br><span class="accent">finance team</span> and<br>increasing profit.</p>
      <span class="btn btn--solid">Get started</span>
    </div>
  </section>
  <section class="m-sec m-services">
    <h2 class="head sec-title">Our Services</h2>
    <p class="kicker">What we do</p>
    <div class="m-card" style="top:62px">
      <div class="photo" role="img" aria-label="Photo of a small model house on coins beside a calculator" style="background:linear-gradient(160deg,#e8e2d6,#b79c76 60%,#5f7b5a)"></div>
      <h3>Financial Models</h3>
      <p class="body-text">Lorem ipsum dolor sit amet, consecte-<br>tur adipiscing elit, sed do eiusmod<br>tempor incididunt.</p>
      <span class="btn">Learn more</span>
    </div>
    <div class="m-card" style="top:291px">
      <div class="photo" role="img" aria-label="Photo of hands reviewing printed budget charts" style="background:linear-gradient(160deg,#2a3440,#a9bccb 55%,#e6ecf1)"></div>
      <h3>Budgeting Process</h3>
      <p class="body-text">Lorem ipsum dolor sit amet, consecte-<br>tur adipiscing elit, sed do eiusmod<br>tempor incididunt.</p>
      <span class="btn btn--solid">Learn more</span>
    </div>
    <div class="m-card" style="top:519px">
      <div class="photo" role="img" aria-label="Illustration of a network of staff figures above an open hand" style="background:linear-gradient(160deg,#9fb6cc,#5d7b99 55%,#c8a98a)"></div>
      <h3>Temporary Staffing</h3>
      <p class="body-text">Lorem ipsum dolor sit amet, consecte-<br>tur adipiscing elit, sed do eiusmod<br>tempor incididunt.</p>
      <span class="btn">Learn more</span>
    </div>
    <div class="m-card" style="top:748px">
      <div class="photo" role="img" aria-label="Illustration of a figure inside a glowing digital data sphere" style="background:radial-gradient(circle at 50% 45%,#6fb7e8,#1f4f80 55%,#0c2037)"></div>
      <h3>Data Cleansing</h3>
      <p class="body-text">Lorem ipsum dolor sit amet, consecte-<br>tur adipiscing elit, sed do eiusmod<br>tempor incididunt.</p>
      <span class="btn">Learn more</span>
    </div>
    <div class="more"><span class="btn btn--solid">View all services</span></div>
  </section>
  <section class="m-sec m-about">
    <h2 class="head">About Kelvane<br>Consulting.</h2>
    <p class="kicker">Who we are</p>
    <p class="body-text">I am an experienced Finance professional who develops strategic financial plans, provides insightful analysis, and supports decision-making. With over 10 years of experience, I have successfully increased profitability for clients by $17M.</p>
    <p class="body-text">Error sit voluptatem accusantium doloremque laudantium, totam rem aperiam, eaque ipsa quae ab illo inventore veritatis et quasi architecto beatae vitae dicta sunt explicabo. Nemo enim ipsam voluptatem quia voluptas sit aspernatur aut odit aut.</p>
    <span class="btn btn--light">Learn more</span>
    <div class="photo" role="img" aria-label="Photo of a consultant smiling in a meeting with a client" style="background:linear-gradient(120deg,#f1ede8,#c9a98c 55%,#7d6a5c)"></div>
    <span class="about-badge"></span>
  </section>
  <section class="m-sec m-contact">
    <h2 class="head">Contact Us</h2>
    <p class="kicker">Get in touch</p>
    <div class="m-info">
      <div><svg class="icon" viewBox="0 0 10 10"><path d="M5 0a3.5 3.5 0 0 0-3.5 3.5C1.5 6 5 10 5 10s3.5-4 3.5-6.5A3.5 3.5 0 0 0 5 0zm0 5a1.5 1.5 0 1 1 0-3 1.5 1.5 0 0 1 0 3z" fill="#1a9be6"/></svg><span>123 Lorem ipsum dolor sit amet,<br>consectetur adipiscing.</span></div>
      <div><svg class="icon" viewBox="0 0 10 10"><path d="M2 0l2 2.5-1 1.5a6 6 0 0 0 3 3l1.5-1L10 8l-1 2C4 10 0 6 0 1z" fill="#1a9be6"/></svg><span>+1 888 888 8888</span></div>
      <div><svg class="icon" viewBox="0 0 10 10"><path d="M0 2h10v6H0z" fill="#1a9be6"/><path d="M0 2l5 3.5L10 2" stroke="#fff" fill="none" stroke-width=".8"/></svg><span>hello@kelvaneconsult.com</span></div>
    </div>
    <div class="m-form">
      <div class="field">First Name</div>
      <div class="field">Last Name</div>
      <div class="field">Email Address</div>
      <div class="field">Phone Number</div>
      <div class="field field--msg">Message</div>
      <span class="btn btn--solid submit">Submit now</span>
    </div>
  </section>
  <footer class="m-sec m-footer">
    <div class="brand"><span class="brand-mark"></span><span>Kelvane Consulting</span></div>
    <div class="m-finfo">
      <div><span class="dot-icon"></span><span>123 Lorem ipsum dolor sit amet<br>consectetur adipiscing elit.</span></div>
      <div><span class="dot-icon"></span><span>Telephone: +1 888 888 8888</span></div>
      <div><span class="dot-icon"></span><span>Email Us<br>hello@kelvaneconsult.com</span></div>
    </div>
    <span class="footer-rule" style="top:160px"></span>
    <nav class="m-flinks"><span>HOME</span><span>ABOUT US</span><span>OUR SERVICES</span><span>BLOG</span><span>CONTACT</span><span>CAREERS</span></nav>
    <span class="footer-rule" style="top:290px"></span>
    <p class="copy">Copyright © 2023 Kelvane Consulting<br>All Rights Reserved</p>
    <div class="socials"><span></span><span></span><span></span><span></span></div>
  </footer>
</div>

<!-- ================= WEB (DARK) ================= -->
<div class="site site--dark">
  <div class="sec topbar">
    <span class="topbar-blue"></span>
    <div class="socials"><span></span><span></span><span></span><span></span></div>
    <div class="topbar-info"><span>+1 888 888 8888</span><span>hello@kelvaneconsult.com</span></div>
  </div>
  <nav class="sec nav">
    <div class="nav-links nav-links--left"><span>Home</span><span>About Us</span><span>Our Services</span></div>
    <div class="brand"><span class="brand-mark"></span><span>Kelvane Consulting</span></div>
    <div class="nav-links nav-links--right"><span>Blog</span><span>Contact Us</span><span class="btn">Get in touch</span></div>
  </nav>
  <section class="sec hero">
    <div class="hero-photo" role="img" aria-label="Photo of a smiling businesswoman at a laptop with a male colleague in a bright office"></div>
    <div class="hero-dots"><span></span><span></span><span></span><span></span><span class="on"></span></div>
    <div class="hero-copy">
      <p class="head">Helping <span class="accent">your</span><br><span class="accent">finance team</span> and<br>increasing profit.</p>
      <p class="body-text">Lorem ipsum dolor sit amet, consectetur adipiscing elit, sed do eiusmod tempor incid idunt ut labore et dolore magna aliqua.</p>
      <span class="btn btn--solid">Get started</span>
    </div>
  </section>
  <section class="sec services">
    <h2 class="head sec-title">Our Services</h2>
    <p class="kicker">What we do</p>
    <div class="cards">
      <div class="card"><div class="photo" role="img" aria-label="Photo of a small model house on coins beside a calculator" style="background:linear-gradient(160deg,#e8e2d6,#b79c76 60%,#5f7b5a)"></div><h3>Financial Models</h3><p class="body-text">Lorem ipsum dolor sit amet, consecte-<br>tur adipiscing elit, sed do eiusmod<br>tempor incididunt.</p><span class="btn">Learn more</span></div>
      <div class="card"><div class="photo" role="img" aria-label="Photo of hands reviewing printed budget charts" style="background:linear-gradient(160deg,#2a3440,#a9bccb 55%,#e6ecf1)"></div><h3>Budgeting Process</h3><p class="body-text">Lorem ipsum dolor sit amet, consecte-<br>tur adipiscing elit, sed do eiusmod<br>tempor incididunt.</p><span class="btn btn--solid">Learn more</span></div>
      <div class="card"><div class="photo" role="img" aria-label="Illustration of a network of staff figures above an open hand" style="background:linear-gradient(160deg,#9fb6cc,#5d7b99 55%,#c8a98a)"></div><h3>Temporary Staffing</h3><p class="body-text">Lorem ipsum dolor sit amet, consecte-<br>tur adipiscing elit, sed do eiusmod<br>tempor incididunt.</p><span class="btn">Learn more</span></div>
      <div class="card"><div class="photo" role="img" aria-label="Illustration of a figure inside a glowing digital data sphere" style="background:radial-gradient(circle at 50% 45%,#6fb7e8,#1f4f80 55%,#0c2037)"></div><h3>Data Cleansing</h3><p class="body-text">Lorem ipsum dolor sit amet, consecte-<br>tur adipiscing elit, sed do eiusmod<br>tempor incididunt.</p><span class="btn">Learn more</span></div>
    </div>
    <div class="more"><span class="btn btn--solid">View all services</span></div>
  </section>
  <section class="sec about">
    <div class="photo" role="img" aria-label="Photo of a consultant smiling in a meeting with a client" style="background:linear-gradient(120deg,#f1ede8,#c9a98c 55%,#7d6a5c)"></div>
    <span class="about-badge"></span>
    <div class="about-copy">
      <h2 class="head">About Kelvane<br>Consulting.</h2>
      <p class="kicker">Who we are</p>
      <p class="body-text">I am an experienced Finance professional who develops strategic financial plans, provides insightful analysis, and supports decision-making. With over 10 years of experience, I have successfully increased profitability for clients by $17M.</p>
      <p class="body-text">Error sit voluptatem accusantium doloremque laudantium, totam rem aperiam, eaque ipsa quae ab illo inventore veritatis et quasi architecto beatae vitae dicta sunt explicabo. Nemo enim ipsam voluptatem quia voluptas sit aspernatur aut odit aut.</p>
      <span class="btn btn--light">Learn more</span>
    </div>
  </section>
  <section class="sec contact">
    <h2 class="head sec-title">Contact Us</h2>
    <p class="kicker">Get in touch</p>
    <div class="contact-info">
      <div><svg class="icon" viewBox="0 0 10 10"><path d="M5 0a3.5 3.5 0 0 0-3.5 3.5C1.5 6 5 10 5 10s3.5-4 3.5-6.5A3.5 3.5 0 0 0 5 0zm0 5a1.5 1.5 0 1 1 0-3 1.5 1.5 0 0 1 0 3z" fill="#1a9be6"/></svg><span>123 Lorem ipsum dolor sit amet,<br>consectetur adipiscing.</span></div>
      <div><svg class="icon" viewBox="0 0 10 10"><path d="M2 0l2 2.5-1 1.5a6 6 0 0 0 3 3l1.5-1L10 8l-1 2C4 10 0 6 0 1z" fill="#1a9be6"/></svg><span>+1 888 888 8888</span></div>
      <div><svg class="icon" viewBox="0 0 10 10"><path d="M0 2h10v6H0z" fill="#1a9be6"/><path d="M0 2l5 3.5L10 2" stroke="#fff" fill="none" stroke-width=".8"/></svg><span>hello@kelvaneconsult.com</span></div>
    </div>
    <div class="form">
      <div class="field">First Name</div><div class="field">Last Name</div>
      <div class="field">Email Address</div><div class="field">Phone Number</div>
      <div class="field field--msg">Message</div>
      <span class="btn btn--solid submit">Submit now</span>
    </div>
  </section>
  <footer class="sec footer">
    <div class="brand"><span class="brand-mark"></span><span>Kelvane Consulting</span></div>
    <div class="footer-info">
      <div><span class="dot-icon"></span><span>123 Lorem ipsum dolor sit amet<br>consectetur adipiscing elit.</span></div>
      <div><span class="dot-icon"></span><span>Telephone: +1 888 888 8888</span></div>
      <div><span class="dot-icon"></span><span>Email Us<br>hello@kelvaneconsult.com</span></div>
    </div>
    <span class="footer-rule" style="top:110px"></span>
    <nav class="footer-links"><span>Home</span><span>About Us</span><span>Our Services</span><span>Blog</span><span>Contact</span><span>Careers</span></nav>
    <span class="footer-rule" style="top:143px"></span>
    <p class="copy">Copyright © 2023 Kelvane Consulting. All Rights Reserved</p>
    <div class="socials"><span></span><span></span><span></span><span></span></div>
  </footer>
</div>

<!-- ================= WEB (LIGHT) ================= -->
<div class="site site--light">
  <div class="sec topbar">
    <span class="topbar-blue"></span>
    <div class="socials"><span></span><span></span><span></span><span></span></div>
    <div class="topbar-info"><span>+1 888 888 8888</span><span>hello@kelvaneconsult.com</span></div>
  </div>
  <nav class="sec nav">
    <div class="nav-links nav-links--left"><span>Home</span><span>About Us</span><span>Our Services</span></div>
    <div class="brand"><span class="brand-mark"></span><span>Kelvane Consulting</span></div>
    <div class="nav-links nav-links--right"><span>Blog</span><span>Contact Us</span><span class="btn">Get in touch</span></div>
  </nav>
  <section class="sec hero">
    <div class="hero-photo" role="img" aria-label="Photo of a smiling businesswoman at a laptop with a male colleague in a bright office"></div>
    <div class="hero-dots"><span></span><span></span><span></span><span></span><span class="on"></span></div>
    <div class="hero-copy">
      <p class="head">Helping <span class="accent">your</span><br><span class="accent">finance team</span> and<br>increasing profit.</p>
      <p class="body-text">Lorem ipsum dolor sit amet, consectetur adipiscing elit, sed do eiusmod tempor incid idunt ut labore et dolore magna aliqua.</p>
      <span class="btn btn--solid">Get started</span>
    </div>
  </section>
  <section class="sec services">
    <h2 class="head sec-title">Our Services</h2>
    <p class="kicker">What we do</p>
    <div class="cards">
      <div class="card"><div class="photo" role="img" aria-label="Photo of a small model house on coins beside a calculator" style="background:linear-gradient(160deg,#e8e2d6,#b79c76 60%,#5f7b5a)"></div><h3>Financial Models</h3><p class="body-text">Lorem ipsum dolor sit amet, consecte-<br>tur adipiscing elit, sed do eiusmod<br>tempor incididunt.</p><span class="btn">Learn more</span></div>
      <div class="card"><div class="photo" role="img" aria-label="Photo of hands reviewing printed budget charts" style="background:linear-gradient(160deg,#2a3440,#a9bccb 55%,#e6ecf1)"></div><h3>Budgeting Process</h3><p class="body-text">Lorem ipsum dolor sit amet, consecte-<br>tur adipiscing elit, sed do eiusmod<br>tempor incididunt.</p><span class="btn btn--solid">Learn more</span></div>
      <div class="card"><div class="photo" role="img" aria-label="Illustration of a network of staff figures above an open hand" style="background:linear-gradient(160deg,#9fb6cc,#5d7b99 55%,#c8a98a)"></div><h3>Temporary Staffing</h3><p class="body-text">Lorem ipsum dolor sit amet, consecte-<br>tur adipiscing elit, sed do eiusmod<br>tempor incididunt.</p><span class="btn">Learn more</span></div>
      <div class="card"><div class="photo" role="img" aria-label="Illustration of a figure inside a glowing digital data sphere" style="background:radial-gradient(circle at 50% 45%,#6fb7e8,#1f4f80 55%,#0c2037)"></div><h3>Data Cleansing</h3><p class="body-text">Lorem ipsum dolor sit amet, consecte-<br>tur adipiscing elit, sed do eiusmod<br>tempor incididunt.</p><span class="btn">Learn more</span></div>
    </div>
    <div class="more"><span class="btn btn--solid">View all services</span></div>
  </section>
  <section class="sec about">
    <div class="photo" role="img" aria-label="Photo of a consultant smiling in a meeting with a client" style="background:linear-gradient(120deg,#f1ede8,#c9a98c 55%,#7d6a5c)"></div>
    <span class="about-badge"></span>
    <div class="about-copy">
      <h2 class="head">About Kelvane<br>Consulting.</h2>
      <p class="kicker">Who we are</p>
      <p class="body-text">I am an experienced Finance professional who develops strategic financial plans, provides insightful analysis, and supports decision-making. With over 10 years of experience, I have successfully increased profitability for clients by $17M.</p>
      <p class="body-text">Error sit voluptatem accusantium doloremque laudantium, totam rem aperiam, eaque ipsa quae ab illo inventore veritatis et quasi architecto beatae vitae dicta sunt explicabo. Nemo enim ipsam voluptatem quia voluptas sit aspernatur aut odit aut.</p>
      <span class="btn btn--light">Learn more</span>
    </div>
  </section>
  <section class="sec contact">
    <h2 class="head sec-title">Contact Us</h2>
    <p class="kicker">Get in touch</p>
    <div class="contact-info">
      <div><svg class="icon" viewBox="0 0 10 10"><path d="M5 0a3.5 3.5 0 0 0-3.5 3.5C1.5 6 5 10 5 10s3.5-4 3.5-6.5A3.5 3.5 0 0 0 5 0zm0 5a1.5 1.5 0 1 1 0-3 1.5 1.5 0 0 1 0 3z" fill="#1a9be6"/></svg><span>123 Lorem ipsum dolor sit amet,<br>consectetur adipiscing.</span></div>
      <div><svg class="icon" viewBox="0 0 10 10"><path d="M2 0l2 2.5-1 1.5a6 6 0 0 0 3 3l1.5-1L10 8l-1 2C4 10 0 6 0 1z" fill="#1a9be6"/></svg><span>+1 888 888 8888</span></div>
      <div><svg class="icon" viewBox="0 0 10 10"><path d="M0 2h10v6H0z" fill="#1a9be6"/><path d="M0 2l5 3.5L10 2" stroke="#fff" fill="none" stroke-width=".8"/></svg><span>hello@kelvaneconsult.com</span></div>
    </div>
    <div class="form">
      <div class="field">First Name</div><div class="field">Last Name</div>
      <div class="field">Email Address</div><div class="field">Phone Number</div>
      <div class="field field--msg">Message</div>
      <span class="btn btn--solid submit">Submit now</span>
    </div>
  </section>
  <footer class="sec footer">
    <div class="brand"><span class="brand-mark"></span><span>Kelvane Consulting</span></div>
    <div class="footer-info">
      <div><span class="dot-icon"></span><span>123 Lorem ipsum dolor sit amet<br>consectetur adipiscing elit.</span></div>
      <div><span class="dot-icon"></span><span>Telephone: +1 888 888 8888</span></div>
      <div><span class="dot-icon"></span><span>Email Us<br>hello@kelvaneconsult.com</span></div>
    </div>
    <span class="footer-rule" style="top:110px"></span>
    <nav class="footer-links"><span>Home</span><span>About Us</span><span>Our Services</span><span>Blog</span><span>Contact</span><span>Careers</span></nav>
    <span class="footer-rule" style="top:143px"></span>
    <p class="copy">Copyright © 2023 Kelvane Consulting. All Rights Reserved</p>
    <div class="socials"><span></span><span></span><span></span><span></span></div>
  </footer>
</div>

<p class="board-thanks">Thank You For Watching</p>
</body>
</html>
```